simple attractive bottled purified natural water label

Looking for a logo design, for a bottled water house brand.The Name of the water is "Orvi-K" Natural Purified water I have attached 2 images, In the Tamsol Image, I Like the top Left water design, the bold Red Name really stands out.I like the placement of the Font with the Natural Purified water,On the 2nd image Russian one, I again like the red bold, the bird flying out is interesting, not sure if a concept could rather use a seabird / gul or a albatros type, with the same effectThe blue colours in bother these designs are great.Many tahnks

Target Market(s)

Young crowd

Font styles to use
Sans Serif

Colors
0455a3
3276b5
ffffff
33a6d7
85cae6
85acd3
0692cd
ec1f27

Requirements
Must have
• some red in the label to make it pop.
• simple design
Nice to have
• the idea of a Gull ( Bird ) flying out to signify free pure natural.

```html
<!DOCTYPE html>
<html lang="en">
<head>
<meta charset="utf-8">
<title>Orvi-K Natural Purified Water Label</title>
<link rel="stylesheet" href="https://fonts.googleapis.com/css2?family=Montserrat:wght@800;900&display=swap">
<style>
  :root {
    --navy: #0455a3;
    --mid-blue: #3276b5;
    --sky: #33a6d7;
    --ice: #85cae6;
    --ocean: #0692cd;
    --white: #ffffff;
    --red: #ec1f27;
    --page: #ffffff;
  }
  * { margin: 0; padding: 0; box-sizing: border-box; }
  html, body {
    width: 1200px; height: 1200px; overflow: hidden;
    background: var(--page);
    font-family: "Montserrat", Arial, sans-serif;
  }
  .label {
    position: absolute;
    left: 40px; top: 224px;
    width: 1120px; height: 752px;
    overflow: hidden;
  }
  .label-background {
    position: absolute; inset: 0;
    background: linear-gradient(120deg, var(--ice) 0%, var(--sky) 45%, var(--mid-blue) 75%, var(--navy) 100%);
  }
  .brand-small {
    position: absolute; left: 22px; top: 14px;
    font-size: 36px; font-weight: 900; color: var(--white);
    letter-spacing: 1px;
  }
  .brand-mark {
    position: absolute; left: 108px; top: 300px;
    width: 160px; height: 160px; border-radius: 50%;
    background: var(--red);
  }
  .brand-name {
    position: absolute; left: 300px; top: 290px;
    font-size: 180px; font-weight: 900; line-height: 1;
    color: var(--red); letter-spacing: 2px;
    white-space: nowrap;
  }
  .product-type {
    position: absolute; left: 280px; width: 720px; top: 482px;
    text-align: center;
    font-size: 38px; font-weight: 800; color: var(--white);
    letter-spacing: 1px; white-space: nowrap;
  }
  .tagline {
    position: absolute; left: 292px; top: 640px;
    font-size: 36px; font-weight: 800; line-height: 1.25;
    color: var(--white); letter-spacing: 0.5px;
    white-space: nowrap;
  }
</style>
</head>
<body>
  <div class="label">
    <div class="label-background" role="img" aria-label="Water background with bubbles and flowing blue waves"></div>
    <div class="brand-small">ORVI-K</div>
    <div class="brand-mark"></div>
    <div class="brand-name">ORVI-K</div>
    <div class="product-type">NATURAL PURIFIED WATER</div>
    <p class="tagline">LOREM IPSUM DOLOR SIT AMET,<br>CONSECTETUR ADIPISCING ELIT</p>
  </div>
</body>
</html>
```